Australian Natural Therpaist needs a light, fun, inviting wordpress website!

I need a wordpress website for my natural therapies business. I have already purchased the "pelo" theme from quietbramble.com and so ideally this is what I would like to use.

The website will have the following pages:
1) Home
2) About Me
3) How I can help you
4) Contact Me
5) FAQ
6) Client Stories
7) Blog

I have attached a Balsamiq XML mockup and PDF of the homepage

I want the website to be very friendly and to de-mystify natural therapies/energy healing etc. I would like to keep the hand drawn/cartoon concept as it keeps everything light. My blog posts will consist of hand drawings and cartoons along with the blog text and so this would tie in with the look and feel of the website.

The homepage should have a slider at the top so that I can promote different concepts. The mockup shows an example of one of the advertising concepts I would use.

The website should make you feel light, it should be fun. No unicorns or rainbows. Here is a great example of what I DO NOT WANT http://www.copperwhistle.com/

```html
<!DOCTYPE html>
<html lang="en">
<head>
<meta charset="utf-8">
<title>Rowan Ashby — Healer, Helper, Mentor, Friend</title>
<link rel="stylesheet" href="https://fonts.googleapis.com/css2?family=Open+Sans:ital,wght@0,300;0,400;0,600;0,700;1,400&display=swap">
<style>
:root{
  --teal:#21b9a8;
  --ink:#333333;
  --body:#777777;
  --muted:#999999;
  --light:#f5f5f5;
  --line:#e4e4e4;
  --dark:#333333;
  --darker:#2a2a2a;
  --field:#262626;
  --white:#ffffff;
}
*{margin:0;padding:0;box-sizing:border-box}
html,body{width:1200px;height:2466px;overflow:hidden}
body{font-family:"Open Sans",Arial,sans-serif;color:var(--ink);background:var(--white);position:relative}
.abs{position:absolute}
.teal{color:var(--teal)}
.section-title{font-weight:300;color:var(--teal);line-height:.84}
.copy{font-size:12.5px;line-height:24px;color:var(--body)}

/* header */
.site-header{top:0;left:0;width:1200px;height:80px;background:#f7f7f7;border-bottom:1px solid var(--line)}
.brand{left:76px;top:18px}
.brand-name{font-size:28px;font-weight:400;color:var(--ink);line-height:1.1}
.brand-name span{color:var(--teal)}
.brand-tag{font-size:12px;color:var(--muted);margin-top:4px;letter-spacing:.3px}
.main-nav{top:52px;left:0;font-size:12.5px;color:var(--ink)}
.main-nav a{position:absolute;white-space:nowrap;color:inherit;text-decoration:none}
.main-nav a.current{color:var(--teal)}

/* hero */
.hero{top:80px;left:0;width:1200px;height:494px;background:linear-gradient(100deg,#d9cfc4 0%,#c9b3a1 40%,#a7826a 70%,#6d4c3b 100%)}
.hero-title{top:124px;left:0;width:1200px;text-align:center;font-size:62px;font-weight:400;color:var(--teal);line-height:1.1}
.hero-text{top:198px;left:280px;width:640px;text-align:center;font-size:17px;line-height:22px;color:#222}
.hero-btn{top:278px;left:485px;width:232px;height:43px;background:#3a3a3a;color:var(--white);font-size:18px;line-height:43px;text-align:center;border-radius:2px}
.hero-dots{top:357px;left:567px;display:flex;gap:6px}
.hero-dots i{width:11px;height:11px;border-radius:50%;background:var(--white);display:block}
.hero-dots i.on{background:var(--teal)}

/* about */
.about-photo{top:574px;left:100px;width:295px;height:333px;background:linear-gradient(180deg,#e8e4e0 0%,#2c2c2c 45%,#1e1e1e 100%)}
.about-title{top:644px;left:434px;font-size:46px}
.about-sub{top:731px;left:434px;font-size:16px;color:var(--ink)}
.about-copy{top:758px;left:434px;width:692px}

/* help */
.help{top:907px;left:0;width:1200px;height:326px;background:var(--light)}
.help-title{top:48px;left:69px;font-size:46px}
.help-sub{top:135px;left:74px;font-size:16px;color:var(--ink)}
.help-copy{top:162px;left:74px;width:680px}
.monitor{top:55px;left:797px}

/* questions */
.faq-title{top:1257px;left:69px;font-size:49px;line-height:1.1}
.faq-item{width:290px}
.faq-q{font-size:14px;color:var(--ink)}
.faq-a{font-size:12.5px;line-height:21px;color:var(--body);margin-top:4px}
.faq-art{top:1250px;left:805px;width:313px;height:287px;background:radial-gradient(ellipse at 50% 100%,#e4c8a4 0%,#f2e6d6 40%,#ffffff 75%)}

/* stories */
.stories{top:1537px;left:0;width:1200px;height:304px;background:var(--light)}
.stories-title{top:32px;left:72px;font-size:49px;line-height:1.1}
.stories-sub{top:82px;left:74px;font-size:14px;color:var(--ink)}
.story{top:120px;width:360px}
.story-avatar{position:absolute;left:0;top:3px;width:90px;height:90px;border-radius:50%}
.story-body{position:absolute;left:108px;top:0;width:230px;font-size:12px;line-height:21.5px;font-style:italic;color:var(--body)}
.story-name{position:absolute;left:108px;top:125px;font-size:12px;font-style:italic;color:var(--teal);font-weight:600}
.story-place{position:absolute;left:108px;top:145px;font-size:11px;font-style:italic;color:var(--muted)}

/* blog */
.blog-title{top:1852px;left:70px;font-size:49px;line-height:1.1}
.blog-intro{top:1922px;left:74px;width:230px;font-size:14px;line-height:20px;color:var(--ink)}
.blog-intro-copy{top:1960px;left:74px;width:230px}
.blog-arrows{top:2050px;left:74px;display:flex;gap:8px}
.blog-arrows span{width:30px;height:30px;border-radius:50%;background:#b9b9b9;display:flex;align-items:center;justify-content:center}
.post{top:1863px;width:243px}
.post-image{width:243px;height:121px}
.post-title{margin-top:12px;font-size:14px;font-weight:600;color:var(--teal)}
.post-copy{margin-top:6px;font-size:12.5px;line-height:21px;color:var(--body)}
.post-more{margin-top:12px;font-size:11.5px;font-style:italic;color:var(--teal)}

/* contact */
.contact{top:2131px;left:0;width:1200px;height:266px;background:var(--dark)}
.contact-title{top:20px;left:72px;font-size:49px;line-height:1.1}
.contact-lead{top:80px;left:77px;width:240px;font-size:14px;line-height:20px;color:var(--white)}
.contact-details{top:128px;left:77px;font-size:12px;line-height:22px;color:#cfcfcf}
.contact-map{top:26px;left:348px;width:319px;height:220px;background:linear-gradient(135deg,#e6e2d6 0%,#d6dcc6 50%,#ebe6da 100%)}
.quick-title{top:20px;left:702px;font-size:49px;line-height:1.1}
.field{background:var(--field);border-radius:6px;color:#8a8a8a;font-size:13px;padding:0 14px;line-height:33px;height:33px}
.field.message{line-height:22px;padding-top:6px;height:79px}
.submit{top:210px;left:1026px;width:100px;height:36px;border-radius:5px;background:var(--teal);color:#10302c;font-size:13px;font-weight:700;text-align:center;line-height:36px;letter-spacing:.5px}

/* footer */
.site-footer{top:2397px;left:0;width:1200px;height:69px;background:var(--darker)}
.legal{top:26px;left:76px;font-size:12px;color:#6e6e6e}
.legal strong{color:#8a8a8a;font-weight:600}
.legal .links{color:#d0d0d0}
.social{top:19px;left:962px;display:flex;gap:5px}
.social i{display:block;width:29px;height:29px;border-radius:50%;background:#8a8a8a}
</style>
</head>
<body>

<header class="site-header abs">
  <div class="brand abs">
    <div class="brand-name"><span>Rowan</span> Ashby</div>
    <div class="brand-tag">Healer - Helper - Mentor - Friend</div>
  </div>
  <nav class="main-nav abs">
    <a class="current" style="left:518px">Home</a>
    <a style="left:588px">About Me</a>
    <a style="left:679px">How I Can Help You</a>
    <a style="left:829px">FAQ</a>
    <a style="left:886px">Blog</a>
    <a style="left:947px">Client Stories</a>
    <a style="left:1057px">Contact Me</a>
  </nav>
</header>

<section class="hero abs" role="img" aria-label="Slider photo: a relaxed woman receiving hands-on energy healing">
  <h1 class="hero-title abs">Its Beautiful Here</h1>
  <p class="hero-text abs">Vivamus ipsum velit, ullamcorper quis nibh non, molestie tempus sapien. Mauris ultrices, felis ut eleifend auctor, leo felis vehicula quam, ut accumsan augue nunc at nisl.</p>
  <div class="hero-btn abs">Book a Time Now</div>
  <div class="hero-dots abs"><i class="on"></i><i></i><i></i><i></i></div>
</section>

<div class="about-photo abs" role="img" aria-label="Portrait of the healer in a dark suit holding a glowing light"></div>
<h2 class="section-title about-title abs">About<br>Me</h2>
<p class="about-sub abs">Who &nbsp;is the Rowan Ashby? &nbsp;What’s his story?</p>
<p class="copy about-copy abs">Aliquam molestie, mi et imperdiet euismod, dui purus auctor tellus, et interdum lacus lectus et ante. Sed accumsan sollicitudin sapien, sit amet adipiscing turpis gravida ac. In congue, neque ac lobortis volutpat, libero mauris varius mi, vitae suscipit ipsum ligula vitae risus. Duis aliquam nibh a dui iaculis viverra id a velit. Vivamus egestas risus in magna varius commodo. Sed semper viverra egestas. Etiam pretium porttitor lectus, vel ornare neque porta volutpat.</p>

<section class="help abs">
  <h2 class="section-title help-title abs">How i can<br>help you</h2>
  <p class="help-sub abs">Given up on feeling better? Let me show you something different..</p>
  <p class="copy help-copy abs">Aliquam molestie, mi et imperdiet euismod, dui purus auctor tellus, et interdum lacus lectus et ante. Sed accumsan sollicitudin sapien, sit amet adipiscing turpis gravida ac. In congue, neque ac lobortis volutpat, libero mauris varius mi, vitae suscipit ipsum ligula vitae risus. Duis aliquam nibh a dui iaculis viverra id a velit. Vivamus egestas risus in magna varius commodo. Sed semper viverra egestas. Etiam pretium porttitor lectus, vel ornare neque porta volutpat.</p>
  <svg class="monitor abs" width="329" height="246" viewBox="0 0 329 246">
    <rect x="0" y="0" width="329" height="226" rx="5" fill="#1c1c1c"/>
    <rect x="0" y="196" width="329" height="30" rx="4" fill="#d9d9d9"/>
    <rect x="0" y="196" width="329" height="4" fill="#bdbdbd"/>
    <rect x="20" y="12" width="289" height="170" fill="#6b5a3e" role="img" aria-label="Video still: a therapist treating a client lying on a couch"/>
    <circle cx="164" cy="97" r="24" fill="none" stroke="#fff" stroke-width="4"/>
    <path d="M156 84 L177 97 L156 110 Z" fill="#fff"/>
    <path d="M130 226 L199 226 L205 246 L124 246 Z" fill="#c8c8c8"/>
  </svg>
</section>

<h2 class="section-title faq-title abs">I have Questions</h2>
<div class="faq-item abs" style="top:1322px;left:74px">
  <p class="faq-q"><span class="teal">Q1:</span> How does all this work?</p>
  <p class="faq-a"><span class="teal">A1:</span> Aliquam molestie, mi et imperdiet euismod, dui purus auctor tellus, et interdum lacus lectus et ante.</p>
</div>
<div class="faq-item abs" style="top:1322px;left:434px">
  <p class="faq-q"><span class="teal">Q3:</span> How does all this work?</p>
  <p class="faq-a"><span class="teal">A3:</span> Aliquam molestie, mi et imperdiet euismod, dui purus auctor tellus, et interdum lacus lectus et ante.</p>
</div>
<div class="faq-item abs" style="top:1427px;left:74px">
  <p class="faq-q"><span class="teal">Q2:</span> How does all this work?</p>
  <p class="faq-a"><span class="teal">A2:</span> Aliquam molestie, mi et imperdiet euismod, dui purus auctor tellus, et interdum lacus lectus et ante.</p>
</div>
<div class="faq-item abs" style="top:1427px;left:434px">
  <p class="faq-q"><span class="teal">Q4:</span> How does all this work?</p>
  <p class="faq-a"><span class="teal">A4:</span> Aliquam molestie, mi et imperdiet euismod, dui purus auctor tellus, et interdum lacus lectus et ante.</p>
</div>
<div class="faq-art abs" role="img" aria-label="Illustration: a woman peeking up at hand-drawn question marks"></div>

<section class="stories abs">
  <h2 class="section-title stories-title abs">Success Stories</h2>
  <p class="stories-sub abs">How have others gone from sad to happy?</p>
  <div class="story abs" style="left:74px">
    <div class="story-avatar" style="background:#6b4a3a" role="img" aria-label="Client portrait"></div>
    <p class="story-body">Vestibulum vel metus sit amet turpis bibendum tincidunt vel sit amet quam. Pellentesque habitant morbi tristique senectus et netus et malesuada fames ac turpis egestas.</p>
    <p class="story-name">-Samantha</p>
    <p class="story-place">Location goes here</p>
  </div>
  <div class="story abs" style="left:434px">
    <div class="story-avatar" style="background:#c9b2a0" role="img" aria-label="Client portrait"></div>
    <p class="story-body">Vestibulum vel metus sit amet turpis bibendum tincidunt vel sit amet quam. Pellentesque habitant morbi tristique senectus et netus et malesuada fames ac turpis egestas.</p>
    <p class="story-name">-Martin</p>
    <p class="story-place">Location goes here</p>
  </div>
  <div class="story abs" style="left:794px">
    <div class="story-avatar" style="background:#8a6a55" role="img" aria-label="Client portrait"></div>
    <p class="story-body">Vestibulum vel metus sit amet turpis bibendum tincidunt vel sit amet quam. Pellentesque habitant morbi tristique senectus et netus et malesuada fames ac turpis egestas.</p>
    <p class="story-name">-Samantha</p>
    <p class="story-place">Location goes here</p>
  </div>
</section>

<h2 class="section-title blog-title abs">Blog</h2>
<p class="blog-intro abs">Want to know the details of how this all works?</p>
<p class="copy blog-intro-copy abs" style="line-height:21px">Aliquam molestie, mi et imperdiet euismod, dui purus auctor tellus, et interdum lacus lectus et ante.</p>
<div class="blog-arrows abs">
  <span><svg width="10" height="12" viewBox="0 0 10 12"><path d="M8 1 L2 6 L8 11" fill="none" stroke="#fff" stroke-width="2.5"/></svg></span>
  <span><svg width="10" height="12" viewBox="0 0 10 12"><path d="M2 1 L8 6 L2 11" fill="none" stroke="#fff" stroke-width="2.5"/></svg></span>
</div>
<article class="post abs" style="left:344px">
  <div class="post-image" style="background:linear-gradient(135deg,#0b1f5a,#2b4fa8 60%,#c89a7a)" role="img" aria-label="Blog image: open hand under sparkling stars"></div>
  <h3 class="post-title">Morbi iaculis fringilla gravida</h3>
  <p class="post-copy">Aliquam molestie, mi et imperdiet euismod, dui purus auctor tellus, et interdum lacus lectus et ante...</p>
  <p class="post-more">Read More</p>
</article>
<article class="post abs" style="left:613px">
  <div class="post-image" style="background:linear-gradient(135deg,#dfe6ee,#cdb8a6 60%,#e9ecef)" role="img" aria-label="Blog image: relaxing head massage"></div>
  <h3 class="post-title">Morbi iaculis fringilla gravida</h3>
  <p class="post-copy">Aliquam molestie, mi et imperdiet euismod, dui purus auctor tellus, et interdum lacus lectus et ante...</p>
  <p class="post-more">Read More</p>
</article>
<article class="post abs" style="left:883px">
  <div class="post-image" style="background:linear-gradient(135deg,#3a1a1a,#8a3a3a 50%,#4a2a4a)" role="img" aria-label="Blog image: candles and cards on a cloth"></div>
  <h3 class="post-title">Morbi iaculis fringilla gravida</h3>
  <p class="post-copy">Aliquam molestie, mi et imperdiet euismod, dui purus auctor tellus, et interdum lacus lectus et ante...</p>
  <p class="post-more">Read More</p>
</article>

<section class="contact abs">
  <h2 class="section-title contact-title abs">Contact Me</h2>
  <p class="contact-lead abs">Your better can start today. Book a time now.</p>
  <div class="contact-details abs">
    <div class="teal" style="font-weight:600">Rowan Ashby</div>
    <div>42 Fernlea Road</div>
    <div>Road,Harrowby, D04 12KT.</div>
    <div style="margin-top:6px"><span class="teal">Tel:</span> +1 800 555 0142</div>
    <div style="margin-top:4px"><span class="teal">Email:</span> info@rowanashby.com</div>
  </div>
  <div class="contact-map abs" role="img" aria-label="Street map showing the clinic location"></div>
  <h2 class="section-title quick-title abs">Quick Contact</h2>
  <div class="field abs" style="top:85px;left:705px;width:204px">Name</div>
  <div class="field abs" style="top:85px;left:922px;width:204px">Email Address</div>
  <div class="field abs" style="top:126px;left:705px;width:204px">Contact No</div>
  <div class="field abs" style="top:126px;left:922px;width:204px">City</div>
  <div class="field message abs" style="top:167px;left:705px;width:304px">Message</div>
  <div class="submit abs">SUBMIT</div>
</section>

<footer class="site-footer abs">
  <p class="legal abs">Copyright © 2014. <strong>Rowan Ashby.</strong> All Right Reserved. &nbsp;<span class="links">Home &nbsp;| &nbsp;About &nbsp;| &nbsp;Site Map</span></p>
  <div class="social abs"><i></i><i></i><i></i><i></i><i></i></div>
</footer>

</body>
</html>
```